Velvetorchid Hair & Beauty Business Card

Velvetorchid Hair & Beauty is a boutique salon located in the picturesque Lake Taupo NZ. The salon is very luxurious, opulent gold gilded mirrors, chandelier lit, contemporary french decor, sets the mood to create beautiful hair, makeup and all beauty services. Just had a new logo design and now after a new business card.
Logo
14 Korowhai Street
Taupo
Phone (07) 548 6193
www.velvetorchid.co.nz
email hair@velvetorchid.co.nz
Marlena Swithin
Also need a space to put in Stylist name, date, appointment time. thanks;)
Another idea is we could incorporate the wallpaper in the back ground either on the back or front or use an ornate glided frame (around the edge of the card) like on my website where my brides photos flash.
Decided against the wall paper but at least you can see our colour theme for the salon.
Updates

Please check out my updated brief . Thanks :)

Target Market(s)

25-60 years plus, mainly mid age females , wanting the best possible service , high standard of workmanship and money not a problem.

Industry/Entity Type

Boutique

Requirements
Must have
• Gold and silver

```html
<!DOCTYPE html>
<html lang="en">
<head>
<meta charset="utf-8">
<title>Velvetorchid Hair &amp; Beauty – Business Card</title>
<link href="https://fonts.googleapis.com/css2?family=Lato:wght@300;400;700;900&display=swap" rel="stylesheet">
<style>
  :root {
    --stage: #2b2b2b;
    --paper: #ffffff;
    --paper-line: rgba(0,0,0,0.035);
    --ink-black: #070707;
    --gold: #a8892a;
    --gold-bright: #e6cc3a;
    --silver: #6f6f6f;
    --silver-light: #8c8c8c;
    --grey-text: #5a5a5a;
  }
  * { box-sizing: border-box; margin: 0; padding: 0; }
  html, body { width: 1200px; height: 900px; overflow: hidden; }
  body {
    background: var(--stage);
    font-family: "Lato", Arial, sans-serif;
    position: relative;
  }
  .card {
    position: absolute;
    left: 270px;
    width: 660px;
    height: 377px;
    overflow: hidden;
    box-shadow: 0 6px 18px rgba(0,0,0,0.45);
  }
  .paper {
    background-color: var(--paper);
    background-image: repeating-linear-gradient(135deg, var(--paper-line) 0 1px, transparent 1px 4px);
  }

  /* Appointment side */
  .appointment { top: 52px; }
  .appointment-label {
    position: absolute; left: 248px; top: 38px;
    background: var(--gold); color: #fff;
    font-weight: 700; font-size: 17px; letter-spacing: 0.5px;
    padding: 3px 10px;
  }
  .field-row {
    position: absolute; left: 44px; right: 40px;
    display: flex; align-items: center; gap: 10px;
    font-weight: 700; color: var(--silver); font-size: 15px;
  }
  .field-row.date-row { top: 92px; }
  .field-row.days-row { top: 140px; gap: 18px; }
  .field-row.stylist-row { top: 190px; }
  .dots { flex: 1; border-bottom: 2px dotted var(--silver-light); height: 12px; }
  .dots.short { flex: 0 0 150px; }
  .tick-box {
    display: inline-block; width: 20px; height: 17px;
    border: 2px solid var(--gold); border-radius: 4px;
    vertical-align: middle; margin-left: 3px;
  }
  .option { white-space: nowrap; }
  .appointment .brand-name { top: 268px; }

  .brand-name {
    position: absolute; left: 0; right: 0; text-align: center;
    font-family: "Lato", Arial, sans-serif;
    font-weight: 300; font-size: 50px; color: var(--grey-text);
    letter-spacing: 0.5px;
  }
  .brand-name .brand-dot {
    display: inline-block; width: 10px; height: 10px; border-radius: 50%;
    background: var(--grey-text); vertical-align: middle; margin-right: 12px;
  }

  /* Contact side */
  .contact { top: 471px; }
  .contact-top { position: absolute; left: 0; top: 0; width: 100%; height: 175px; }
  .contact .brand-name { top: 62px; }
  .contact-bottom {
    position: absolute; left: 0; top: 175px; width: 100%; height: 202px;
    background: var(--ink-black);
  }
  .divider {
    position: absolute; left: 340px; top: 18px; width: 2px; height: 166px;
    background: linear-gradient(to bottom, transparent, var(--gold), transparent);
  }
  .person { position: absolute; left: 40px; top: 36px; width: 280px; }
  .person-name { color: var(--gold-bright); font-weight: 900; font-size: 21px; letter-spacing: 0.3px; }
  .person-role { color: var(--silver-light); font-size: 13px; letter-spacing: 0.5px; margin-top: 2px; }
  .tagline { color: var(--silver); font-weight: 700; font-size: 16px; line-height: 1.4; margin-top: 26px; }
  .details { position: absolute; left: 370px; top: 28px; width: 270px; }
  .address { color: var(--gold-bright); font-weight: 700; font-size: 15px; line-height: 1.3; }
  .contact-line {
    display: flex; align-items: center; gap: 12px;
    color: var(--silver); font-size: 15px; margin-top: 12px;
  }
  .contact-line svg { width: 18px; height: 14px; flex: none; }
  .website { color: var(--silver); font-weight: 700; font-size: 16px; margin-top: 16px; }
  .website strong { color: var(--gold-bright); font-weight: 900; }
</style>
</head>
<body>

<section class="card paper appointment" aria-label="Appointment card">
  <div class="appointment-label">NEXT APPOINTMENT</div>
  <div class="field-row date-row">
    <span>DATE:</span><span class="dots"></span>
    <span>TIME:</span><span class="dots short"></span>
    <span class="option">AM<span class="tick-box"></span></span>
    <span class="option">PM<span class="tick-box"></span></span>
  </div>
  <div class="field-row days-row">
    <span class="option">Mon<span class="tick-box"></span></span>
    <span class="option">Tue<span class="tick-box"></span></span>
    <span class="option">Wed<span class="tick-box"></span></span>
    <span class="option">Thu<span class="tick-box"></span></span>
    <span class="option">Fri<span class="tick-box"></span></span>
    <span class="option">Sat<span class="tick-box"></span></span>
    <span class="option">Sun<span class="tick-box"></span></span>
  </div>
  <div class="field-row stylist-row">
    <span>NAME OF STYLIST:</span><span class="dots"></span>
  </div>
  <div class="brand-name"><span class="brand-dot"></span>Velvetorchid Hair &amp; Beauty</div>
</section>

<section class="card contact" aria-label="Contact card">
  <div class="contact-top paper">
    <div class="brand-name"><span class="brand-dot"></span>Velvetorchid Hair &amp; Beauty</div>
  </div>
  <div class="contact-bottom">
    <div class="person">
      <div class="person-name">MARLENA SWITHIN</div>
      <div class="person-role">DESIGNATION</div>
      <p class="tagline">Leading Wedding, Bridal Hair<br>&amp; Make-up Specialists with<br>complete privacy in Taupo</p>
    </div>
    <div class="divider"></div>
    <div class="details">
      <div class="address">14 Korowhai Street<br>Taupo, New Zealand 3330</div>
      <div class="contact-line">
        <svg viewBox="0 0 18 14" aria-hidden="true"><path fill="#a8892a" d="M2 4c0-2 3-3 7-3s7 1 7 3v1h-3V4c-1-.6-2.4-.8-4-.8S6 3.4 5 4v1H2zM5 6h8l2 7H3z"/><circle cx="9" cy="9.5" r="1.6" fill="#070707"/></svg>
        <span>(07) 548 6193</span>
      </div>
      <div class="contact-line">
        <svg viewBox="0 0 18 14" aria-hidden="true"><rect x="1" y="1" width="16" height="12" fill="#a8892a"/><path d="M1 1l8 6 8-6" fill="none" stroke="#070707" stroke-width="1.4"/></svg>
        <span>hair@velvetorchid.co.nz</span>
      </div>
      <div class="website">www.<strong>velvetorchid</strong>.co.nz</div>
    </div>
  </div>
</section>

</body>
</html>
```